Brochure Design Project

We are a payroll company. We offer a wide variety of products and services:
1. Payroll Processing
2. Employee Direct Deposit
3. Time and attendance
4. HR services
5. Employee Employee Benefits

I'd like to develop a one page template that uses a combination of our logo (attached), colors (attached) and possible a picture. The picture could be shown as an option as it may change based on the product or service.

Target Market(s)

Adults in the United States ages 22-50. Typically these people are accountants, human resource professionals or entrepreneurs. The payroll industry is dominated by 3 large payroll processors, QLM, Wendrafy and Tolvarex. These companies are very impersonal and make it difficult to resolve issues when they arise. We have grown to over 400 clients by being the opposite of the big guys,

Industry/Entity Type

It Company

Font styles to use
Sans Serif

Requirements
Must have
• The brochure can be one or two pages.
Nice to have
• I'll know it when I see it but I can't describe it. I have attached a few brochures that have caught my eye.
Should not have
• No cartoons. No money signs. Hip, new, fresh are words I'd use to describe the winning product. Of the three people I described in my target market, the entrepreneur is the market I'd most like to target.

```html
<!DOCTYPE html>
<html lang="en">
<head>
<meta charset="utf-8">
<title>HR Solutions for your Business – Ledgerline Pay</title>
<link href="https://fonts.googleapis.com/css2?family=Russo+One&family=Play:wght@400;700&family=Saira+Condensed:wght@500&display=swap" rel="stylesheet">
<style>
  :root{
    --navy:#1b2a6e;
    --ink:#1d2b72;
    --green:#8cc63f;
    --paper:#ffffff;
    --band-light:#e9e9ea;
    --band-mid:#dcdcde;
    --band-dark:#cfcfd2;
  }
  *{margin:0;padding:0;box-sizing:border-box}
  html,body{width:927px;height:1200px;overflow:hidden;background:var(--paper)}
  .sheet{position:relative;width:927px;height:1200px;overflow:hidden;color:var(--ink);
    font-family:"Play",sans-serif;font-weight:700}
  .swoosh{position:absolute;inset:0;z-index:0}
  .content{position:relative;z-index:1;padding:8px 0 0 18px}
  h1{font-family:"Russo One",sans-serif;font-weight:400;font-size:27px;line-height:34px;color:var(--navy);letter-spacing:.3px;margin-bottom:12px}
  .intro p,.service{font-size:14.6px;line-height:17px;letter-spacing:.33px;width:830px}
  .intro p{margin-bottom:17px}
  .service{margin-bottom:17px}
  .service .name{display:block}
  h2{font-family:"Russo One",sans-serif;font-weight:400;font-size:26px;line-height:32px;color:var(--navy);letter-spacing:.2px;margin:15px 0 12px -4px}
  .article{font-size:13.4px;line-height:17px;letter-spacing:.3px;width:909px}
  .article p{margin-bottom:17px}
  .article h3{font-size:13.4px;font-weight:700;margin-bottom:17px}
  .footer{position:absolute;left:0;right:0;bottom:0;height:125px;z-index:1}
  .brand{position:absolute;left:22px;top:20px;width:290px;display:flex;align-items:center;gap:12px;
    font-family:"Play",sans-serif;font-weight:700;font-size:44px;line-height:42px;color:var(--navy)}
  .brand .dot{flex:none;width:20px;height:20px;background:var(--navy);border-radius:50%}
  .tagline{position:absolute;left:326px;top:74px;font-family:"Saira Condensed",sans-serif;font-weight:500;font-size:22px;line-height:26px;color:var(--navy)}
  .contact{position:absolute;right:14px;top:8px;width:320px;text-align:center;font-style:normal;font-size:13px;line-height:16.5px;color:var(--navy)}
  .contact .url{display:block;font-family:"Russo One",sans-serif;font-size:26px;line-height:30px;color:var(--green);margin-top:2px;text-align:right}
</style>
</head>
<body>
<div class="sheet">
  <svg class="swoosh" width="927" height="1200" viewBox="0 0 927 1200" aria-hidden="true">
    <defs>
      <linearGradient id="band" x1="0" y1="0" x2="1" y2="0">
        <stop offset="0" stop-color="var(--band-light)" stop-opacity="0"/>
        <stop offset=".6" stop-color="var(--band-mid)"/>
        <stop offset="1" stop-color="var(--band-dark)"/>
      </linearGradient>
    </defs>
    <path d="M300 0 C520 120 700 70 927 20 L927 0Z" fill="url(#band)" opacity=".7"/>
    <path d="M0 420 C300 300 620 200 927 160 L927 330 C650 330 350 420 0 560Z" fill="url(#band)" opacity=".55"/>
    <path d="M0 640 C300 560 620 560 927 640 L927 760 C620 660 300 660 0 760Z" fill="url(#band)" opacity=".45"/>
    <path d="M0 980 C300 900 650 880 927 940 L927 1060 C650 1000 300 1020 0 1090Z" fill="url(#band)" opacity=".4"/>
  </svg>

  <main class="content">
    <section class="intro">
      <h1>HR Solutions for your Business</h1>
      <p>HR PartnerLedgerline Pay provides a customized approach and comprehensive set of HR Solutions for your business.</p>
      <p>Our services are designed to help businesses minimize risk, save money, and eliminate the hassle of managing employee services.</p>
      <div class="service"><span class="name">Employee Screening</span>Pre-employment screening, employee background checks, drug testing and more</div>
      <div class="service"><span class="name">New Hire Reporting</span>Employer reporting for new hires that complies with federal and state laws requirements</div>
      <div class="service"><span class="name">Time &amp; Attendence</span>Automated applications increase accountability, save time and money</div>
      <div class="service"><span class="name">Expense Tracking</span>Integrated expense tracking &amp; reporting</div>
      <div class="service"><span class="name">Customized HR Reporting</span>For increased business intelligence</div>
      <div class="service"><span class="name">Employee Communications</span>For enhanced employee relations</div>
      <div class="service"><span class="name">Employee Self-Service Portal (ESP)</span>The Self-Service Model saves employers time, effort and money while increasing employee satisfaction.</div>
    </section>

    <article class="article">
      <h2>Four Important Benefits of Time and Attendance Applications.</h2>
      <p>Time and Attendance Applications (TAA) are becoming more of a necessity than a luxury.&nbsp; Companies of all sizes can no longer ignore the vast array of features and related cost savings available with these products.&nbsp; The article below summarizes four of the most important benefits TAA can provide.</p>
      <h3>1. Time and Attendance Applications increase Accountability</h3>
      <p>A typical installation process includes a detailed review of all compensation policies and related calculations.&nbsp; The results of that review are programmed to the data collection terminal, which ensures a proper and accurate accounting of all employee hours. Employees and administrators both benefit from the convenience and confidence delivered by these applications.</p>
      <h3>2. Time and Attendance Applications Save Time and Money</h3>
      <p>Gone are the manual and time-consuming ways of inputting employee hours.&nbsp;&nbsp; The automation within these applications, totals employee hours, performs overtime and PTO calculations, and transfers the correct data directly to your payroll company.&nbsp; This integration also eliminates the transfer of manual calculations to the payroll provider, where many costly errors often occur.</p>
      <h3>Reduces Record keeping Burden</h3>
      <p>Unfortunately too many companies learn the hour and wage laws directly from a Department of Labor agent during an investigation or audit.&nbsp; Time and attendance applications, can reduce record-keeping requirements and guarantee compliance with wage and hour laws. All hours and related calculations are stored in the employee's profile and available at your request.</p>
      <h3>Feedback on Employee Behavior</h3>
      <p>Automation, a key component to employee record managment has never been easier or more cost effective.&nbsp; In most cases, the installation of a terminal, similar to the look of a credit card processing machine, is all that's needed for the system to be implemented.&nbsp;&nbsp; Once installed, these systems also detect detrimental employee behavior such as continuing employee absenteeism or other behavior.</p>
      <p>Efficiency, affordability, and convenience have never been easier for those charged with handling the company payroll.&nbsp; Contact us</p>
    </article>
  </main>

  <footer class="footer">
    <div class="brand"><span class="dot"></span><span>Ledgerline<br>Pay</span></div>
    <div class="tagline">Innovative solutions that deliver value</div>
    <address class="contact">
      Ledgerline Pay, Inc.<br>
      58 Harbor Lane, Suite 300<br>
      Alder&nbsp; PA,&nbsp; 19990<br>
      P: 555-014-2270&nbsp;&nbsp;&nbsp; F: 555-014-2271<br>
      E: hello@ledgerlinepay.com
      <span class="url">www.ledgerlinepay.com</span>
    </address>
  </footer>
</div>
</body>
</html>
```